Circle 9 Bloom

I'm looking to get a small booklet done since a brochure doesn't have enough room for the information. I would like for the design to match the information that's provided. Since the information of the booklet is deep and intense I'm looking for someone who's open minded and in the heart. It doesn't have to be complicated. Just eye catching! Thank you :)

• If not us… who? If not now… when?
This is the question many of us are pondering on as we become more and more aware of what’s being purposely done to humanity! Understanding the cause of a problem is the beginning of its solution and that’s exactly what the purpose of the following information provided. It’s unfortunate that most of us don’t realize how we’ve been under the influence of mind control and deprived of our freewill by programs and systems that have been deliberately set in place to control the mass. We’re purposely overloaded with programs and useless information making it very difficult to even have the time to think for ourselves and question what’s really going on. Why do people defend the very systems that have been designed and put in place to control every aspect of our lives if we are not under the influence of mind control? It’s crucial for you to keep that into consideration as you read the following.
Banks, education, governments, the military, religion and the pharmaceutical industry are all corporations that act out on behalf of a few elite families that think of us as nothing more than rodents. Let us observe and reflect on how hatred, war, poverty, disease, obesity, violence, pollution, pornography, depression, and dysfunctional families all have been on the rise in the last hundred years like never before in recorded history! They continually get away with unimaginable crimes done against humanity because they can unlawfully hide behind these corporations. We need to seriously wake up and realize that the systems controlling us are NOT about justice, peace, and freedom but about obedience, force and mind control.
Our masters, the elite, have discovered how to precisely control and manipulate our minds through horrific experiments secretly done to countless human beings by force and against their will. These elites have been at war with our minds for the past century utilizing psychological control tactics also known as neuro linguistic programing (NLP) through technology, advertising, and education. We are continually being bombarded with perverted, sexual, and obscene images that influence our thoughts and behavior. It is believed that by some time in this century, the ability of the mind to successfully differentiate between right and wrong will become all but nonexistent. For a quarter of a century, researchers have been monitoring how our brains react to certain stimuli and how they process information. They have discovered that when the brain starts to get overloaded, it builds up a stubborn wall against sensational stimuli. Modern humanity's exposure to an ever-increasing amount of dramatic, violent, and sensational information, has forced the brain to resort to protecting itself and therefore being conditioned to not question, obey, and follow the majority like dumb sheep.
We all start our lives very curious and highly experimental individuals and then one day forced against our will we are sent into the hands of strangers and institutions of insanity known as schools where we are stripped of our individuality and creativity robbing us of our human rights. Then we turn around and blame the children for how they rebel and behave with their parents instead of questioning why they’re that way. If there were any value to the school institution wouldn’t we be taught things like what are our human rights are, how to grow our own food and preserving it, making others a priority, how to be yourself and confident, mind and heart coherence, the importance and effects of the power of thoughts, words, and our actions, being creative and passion driven, how to cope with stress and emotions, and finally things like love, honesty, compassion, and respect? Do we really think they have our best interest in mind and leading us the right way or is it that we are simply slaves controlled and conditioned to do things against our freewill. We’ve been fooled in thinking that in order to be able to function in society we need to be schooled for 15 to 25 years. The fact and objective of education has always been to dumb us down and to remove our freewill and the influence of family. The education system is nothing more than day prison where we are conditioned to fear, obey, compete, and not question authority. This has all been premeditated and is the prominent cause of our enslavement! The truth is that we are all our own teachers and nothing in our reality has ever been taught into existence as it’s always simply been created and invented by passion driven individual!
We’ve been turned into slaves and consumers in a prison called earth. Most people spend their lifetime in debt, unhealthy, unhappy, and too depressed to question why? Our politicians can fund wars killing the innocent but won’t properly feed and shelter the hungry and needy which is the majority of the planet? Our food has been poisoned to make us sick to then take their medication that addicts and kills us. It’s not a conspiracy but factual that properly and improperly prescribed drugs are on the top of the list of leading causes of death in America. It’s a fact that alcohol is more dangerous than crack and more harmful on the user and others than heroin. Cigarettes have also been proven to kill the user as well as those who don’t smoke because of the second hand smoke. Our water is full of harmful chemicals like chlorine and fluoride. A review of brain studies involving the use of fluoride has concluded that one of the adverse effects of fluoride exposure on children is damage to their neurological development. Sugar, salt, msg, and aspartame are also incredibly toxic and addictive and can found in just about everything product sold at the grocery store. Why are these products still available and legal if they are known to harm and kill us and the people we love and why are the many cures for cancer being suppressed? Our way of communicating with one another has been mostly replaced by technology therefore removing the need for real human contact and affection. It’s sad, but we’ve almost completely forgotten the value of life and how to live. Humanity needs to get back to a more organic way of living before it’s too late. Life has been designed with precision for people to willingly give up their human rights and forget who they are. We have to start making our wellbeing and the wellbeing of others a priority if we want to see the world and our individual realities heal and change for the best.
There may be an object in your home that you unwittingly allow to lead you into a type of hypnotic trance. It’s one of the most popular and destructive devices of our time called the television set. Documentation shows that television’s erotic influence is so pervasive that it increases sexual activity in teens and younger children. Studies show that the age of first sexual intercourse significant decreases due to the influence of TV. The more television watched the lower the age for that first sexual encounter. Not only do studies show it, children themselves report that television encourages them to take part in sexual activity at a young age. Terrible scenes can be shown, but the viewer tends only to laugh or shrug them off being desensitized through exposure. The truth is we are beings who are easily influenced by what we put our focus and attention on. We cannot expect the television industry to reveal the truth about itself, but we do not have to remain uninformed and ignorant about it.
Keeping our eyes and hearts from opening up and seeing the truth behind all the programs that have been created to control and harm us is the reason why sickness and destruction has been so rampant in our bodies and on our planet. How can we truly heal and change if we don’t allow ourselves to see truth behind what’s being done? We are ALL equal and ONE people connected like a body connected by all its parts. Our human rights should always end where others rights begin and no color, tongue, race, or belief should ever separate us. Every feeling, though, word, and action affect us individually and collectively. For the sake of humanity we must get out of our heads and into our hearts where love, peace, and compassion rule. We all are responsible to wake up and take back control of our lives. We are the answer and solution to every problem we face and in order to love and heal the world and others we must first learn to love and heal ourselves.
We understand that the truth is often difficult to hear, however it’s what each and every one of us needs to hear so that we can wake up, heal and transform. Turning away from what is being done to humanity is not the solution to a better world but also part of the problem. We have to stop attacking and judging one another and begin to understand that our battle is not against one another but against these programs and systems destroying us. Now is the time for the people to unite and take action. It’s up to each and every one of us to question everything and do the right thing as we are all responsible for what is being done to humanity and the planet. Our collective and individual reality will transform when we individually realize that we are all connected. For those of you tired of the insanity please feel free to connect with us and express anything that might be on your hearts. We are willing to grow, help, share, and create with all of you who are interested : )

If not us… who? If not now… when?

B You - B Free - B Happy
circle9bloom@quillpost.net

```html
<!DOCTYPE html>
<html lang="en">
<head>
<meta charset="utf-8">
<title>Booklet Spread</title>
<link rel="stylesheet" href="https://fonts.googleapis.com/css2?family=Inter:wght@200;300&display=swap">
<style>
  :root {
    --backdrop: #ececec;
    --plum: #ae5599;
    --plum-text: #f6e3f1;
    --page: #ffffff;
    --body-ink: #5a5a5a;
  }
  html, body {
    margin: 0;
    padding: 0;
    width: 1200px;
    height: 1000px;
    overflow: hidden;
    background: var(--backdrop);
  }
  .spread {
    position: absolute;
    left: 138px;
    top: 126px;
    width: 926px;
    height: 700px;
    display: flex;
  }
  .page-quote {
    width: 463px;
    height: 100%;
    background: var(--plum);
    position: relative;
  }
  .pull-quote {
    position: absolute;
    left: 0;
    right: 0;
    top: 212px;
    margin: 0;
    text-align: center;
    font-family: "Inter", "Helvetica Neue", Arial, sans-serif;
    font-weight: 200;
    font-size: 28px;
    line-height: 40px;
    color: var(--plum-text);
  }
  .page-body {
    width: 463px;
    height: 100%;
    background: var(--page);
    box-sizing: border-box;
    padding: 18px 29px 0 29px;
    overflow: hidden;
  }
  .body-copy {
    margin: 0;
    font-family: "Inter", "Helvetica Neue", Arial, sans-serif;
    font-weight: 300;
    font-size: 14.6px;
    line-height: 26px;
    color: var(--body-ink);
  }
  .body-copy .line {
    display: block;
    white-space: nowrap;
    text-align: justify;
    text-align-last: justify;
  }
</style>
</head>
<body>
  <main class="spread">
    <section class="page-quote">
      <p class="pull-quote">There may be<br>an object in your home that<br>you unwittingly allow to<br>lead you into a type of<br>hypnotic trance.</p>
    </section>
    <section class="page-body">
      <p class="body-copy">
        <span class="line">designed with precision for people to willingly give up</span>
        <span class="line">their human rights and forget who they are. We have</span>
        <span class="line">to start making our wellbeing and the wellbeing of</span>
        <span class="line">others a priority if we want to see the world and our</span>
        <span class="line">individual realities heal and change for the best.</span>
        <span class="line">There may be an object in your home that you</span>
        <span class="line">unwittingly allow to lead you into a type of hypnotic</span>
        <span class="line">trance. It's one of the most popular and destructive</span>
        <span class="line">devices of our time called the television set.</span>
        <span class="line">Documentation shows that television's erotic</span>
        <span class="line">influence is so pervasive that it increases sexual</span>
        <span class="line">activity in teens and younger children. Studies show</span>
        <span class="line">that the age of first sexual intercourse significant</span>
        <span class="line">decreases due to the influence of TV. The more</span>
        <span class="line">television watched the lower the age for that first</span>
        <span class="line">sexual encounter. Not only do studies show it,</span>
        <span class="line">children themselves report that television encourages</span>
        <span class="line">them to take part in sexual activity at a young age.</span>
        <span class="line">Terrible scenes can be shown, but the viewer tends</span>
        <span class="line">only to laugh or shrug them off being desensitized</span>
        <span class="line">through exposure. The truth is we are beings who</span>
        <span class="line">are easily influenced by what we put our focus and</span>
        <span class="line">attention on. We cannot expect the television industry</span>
        <span class="line">to reveal the truth about itself, but we do not have to</span>
      </p>
    </section>
  </main>
</body>
</html>
```